Brookvane Counsel Partners Website Design

I need a website design for my new business consulting and executive coaching firm, Brookvane Counsel Partners. We provide consultative services to business C-suites as well as personal coaching to executives. I have attached the logo with color scheme I have chosen. I would like the website to reflect professionalism and continue the color scheme in the logo.

Target Market(s)

Small to medium business and their executives; middle to upper income men and women in mid- to late career looking for significance

Industry/Entity Type

Business Consultant

Number of Pages Required

4 page

Requirements
Must have
• A homepage with prominent logo and way to contact for more information; an area on the homepage with easy to read, clear text to describe what the company does; a prominent area on the homepage for a tagline; a blog page that can be updated regularly, an "about us" page with biographical information; an "about us" page; a page detailing services offered
• The web design must match the logo colors and font that I have uploaded.
Nice to have
• A lighthouse picture in the background or header
Should not have
• A lot of text area on the homepage

```html
<!DOCTYPE html>
<html lang="en">
<head>
<meta charset="utf-8">
<title>Brookvane Counsel Partners</title>
<link href="https://fonts.googleapis.com/css2?family=Signika:wght@300;400;600&display=swap" rel="stylesheet">
<style>
:root{
  --navy:#1f2f63;
  --maroon:#6e0f14;
  --ink:#4a4a4a;
  --muted:#8a8a8a;
  --light:#f1f1f1;
  --band:#ebebeb;
  --tri:#e9e9e9;
  --line:#e2e2e2;
  --white:#ffffff;
}
*{margin:0;padding:0;box-sizing:border-box}
html,body{width:705px;height:1200px;overflow:hidden;background:var(--white)}
body{position:relative;font-family:"Signika",sans-serif;font-weight:400;color:var(--ink)}
h1,h2{font-weight:400}
.abs{position:absolute}

/* header */
.site-header{position:absolute;left:0;top:0;width:705px;height:72px;background:var(--white)}
.nav-link{position:absolute;top:32px;font-size:8.5px;font-weight:300;color:var(--ink);letter-spacing:.2px;white-space:nowrap;transform:translateX(-50%)}
.nav-link.active{color:var(--navy);font-weight:400}
.nav-link.active::after{content:"";position:absolute;left:-4px;right:-4px;top:18px;height:2px;background:var(--maroon)}
.brand{position:absolute;left:352px;transform:translateX(-50%);display:flex;align-items:center;gap:4px;white-space:nowrap}
.brand-mark{width:7px;height:7px;background:var(--maroon);flex:none}
.brand-name{font-size:7px;font-weight:600;color:var(--navy);letter-spacing:.3px;line-height:1.2;text-align:left}
.search-btn{position:absolute;left:588px;top:22px;width:31px;height:28px;background:var(--navy);color:var(--white);font-size:5px;text-align:center}
.search-btn svg{display:block;margin:6px auto 2px}

/* hero */
.hero{position:absolute;left:0;top:72px;width:705px;height:258px;background:linear-gradient(180deg,#d9dde6 0%,#e8c3c6 35%,#d7879a 52%,#8aa4cc 60%,#4f79b9 80%,#3f67a8 100%)}
.hero-title{position:absolute;left:0;right:0;top:133px;text-align:center;font-size:19px;font-weight:300;color:var(--white);letter-spacing:.5px}
.hero-arrow{position:absolute;top:108px}

/* offer */
.section-title{position:absolute;left:0;right:0;text-align:center;font-size:17px;font-weight:400;color:var(--ink);letter-spacing:.3px}
.offer{position:absolute;top:418px;width:180px;transform:translateX(-50%);text-align:center}
.offer-title{margin-top:9px;font-size:8px;font-weight:400;color:var(--navy);letter-spacing:.2px}
.offer-text{margin-top:11px;font-size:6.4px;line-height:11px;color:var(--muted);font-weight:300}

/* provide */
.provide-band{position:absolute;left:0;top:594px;width:705px;height:316px;background:var(--light)}
.provide-card{position:absolute}
.provide-text{position:absolute;width:248px;font-size:6.4px;line-height:11px;color:var(--muted);font-weight:300}
.plus{position:absolute;left:347px;top:736px;font-size:14px;font-weight:300;color:var(--ink)}

/* newsletter */
.newsletter{position:absolute;left:0;top:910px;width:705px;height:63px;background:var(--band)}
.nl-label{position:absolute;left:124px;top:25px;font-size:9px;font-weight:300;color:var(--ink)}
.nl-input{position:absolute;left:222px;top:18px;width:300px;height:26px;background:var(--white);border:1px solid #ddd;font-size:4.8px;font-weight:300;color:var(--muted);padding:10px 9px}
.nl-button{position:absolute;left:527px;top:18px;width:92px;height:26px;background:var(--maroon);color:var(--white);font-size:8.5px;font-weight:300;text-align:center;line-height:26px}

/* footer */
.footer-rule{position:absolute;left:0;width:705px;height:1px;background:var(--line)}
.footer-brand{position:absolute;left:352px;top:995px;transform:translateX(-50%);background:var(--white);padding:0 10px;display:flex;align-items:center;gap:4px}
.footer-col{position:absolute;top:1047px}
.col-title{font-size:6.5px;font-weight:600;color:var(--navy);padding-bottom:8px;border-bottom:1px solid var(--line);margin-bottom:7px}
.link-list{list-style:none;font-size:5.6px;font-weight:300;color:var(--ink);line-height:14.1px}
.col-text{font-size:5.6px;font-weight:300;line-height:9.5px;color:var(--ink)}
.news-date{font-size:5.6px;font-weight:300;color:var(--maroon);margin-bottom:4px}
.news-item{margin-bottom:10px}
.contact-row{display:flex;gap:13px;font-size:5.6px;font-weight:300;line-height:9.5px;color:var(--ink);margin-bottom:10px}
.contact-row svg{flex:none;margin-top:1px}
.copyright{position:absolute;left:85px;top:1178px;font-size:5.2px;font-weight:300;color:var(--ink)}
.social{position:absolute;left:525px;top:1178px;font-size:5.2px;font-weight:300;color:var(--ink);display:flex;align-items:center;gap:4px}
.social i{display:inline-block;width:5px;height:5px;border-radius:50%;background:#555}
</style>
</head>
<body>

<header class="site-header">
  <span class="nav-link active" style="left:142px">HOME</span>
  <span class="nav-link" style="left:194px">ABOUT US</span>
  <span class="nav-link" style="left:251px">SERVICES</span>
  <div class="brand" style="top:32px">
    <span class="brand-mark"></span>
    <span class="brand-name">BROOKVANE<br>COUNSEL PARTNERS</span>
  </div>
  <span class="nav-link" style="left:421px">CLIENTS</span>
  <span class="nav-link" style="left:484px">TESTIMONIALS</span>
  <span class="nav-link" style="left:549px">CONTACT US</span>
  <div class="search-btn">
    <svg width="8" height="8" viewBox="0 0 10 10"><circle cx="4" cy="4" r="3" fill="none" stroke="#fff" stroke-width="1.6"/><line x1="6.2" y1="6.2" x2="9" y2="9" stroke="#fff" stroke-width="1.8"/></svg>
    SEARCH
  </div>
</header>

<section class="hero" role="img" aria-label="Lighthouse on a rocky shore at dusk, light beam over a calm sea under a pink sky">
  <h1 class="hero-title">BROOKVANE COUNSEL PARTNERS</h1>
  <svg class="hero-arrow" style="left:0" width="38" height="46" viewBox="0 0 38 46"><polygon points="0,0 38,23 0,46" fill="var(--maroon)"/><polyline points="14,17 9,23 14,29" fill="none" stroke="#fff" stroke-width="2"/></svg>
  <svg class="hero-arrow" style="left:667px" width="38" height="46" viewBox="0 0 38 46"><polygon points="38,0 0,23 38,46" fill="var(--maroon)"/><polyline points="24,17 29,23 24,29" fill="none" stroke="#fff" stroke-width="2"/></svg>
</section>

<h2 class="section-title" style="top:367px">WHAT WE OFFER</h2>

<div class="offer" style="left:168px">
  <svg width="92" height="78" viewBox="0 0 92 78">
    <polygon points="46,0 92,78 0,78" fill="var(--tri)"/>
    <circle cx="46" cy="50" r="10" fill="none" stroke="var(--maroon)" stroke-width="1.6"/>
    <text x="46" y="54" text-anchor="middle" font-size="11" font-family="Signika,sans-serif" fill="var(--maroon)">$</text>
  </svg>
  <div class="offer-title">FINANCIAL ACCOUNTING</div>
  <p class="offer-text">Lorem Ipsum is simply dummy text of the printing and typesetting industry. Lorem Ipsum has been the industry's standard dummy text ever</p>
</div>

<div class="offer" style="left:352px">
  <svg width="92" height="78" viewBox="0 0 92 78">
    <polygon points="46,0 92,78 0,78" fill="var(--tri)"/>
    <polyline points="38,48 46,40 54,48 54,56 38,56 38,48" fill="none" stroke="var(--maroon)" stroke-width="1.6" stroke-linejoin="round"/>
    <path d="M33,56 Q40,63 49,62 L58,58" fill="none" stroke="var(--maroon)" stroke-width="1.6"/>
  </svg>
  <div class="offer-title">PROPERTY PROTECTION</div>
  <p class="offer-text">Lorem Ipsum is simply dummy text of the printing and typesetting industry. Lorem Ipsum has been the industry's standard dummy text ever</p>
</div>

<div class="offer" style="left:534px">
  <svg width="92" height="78" viewBox="0 0 92 78">
    <polygon points="46,0 92,78 0,78" fill="var(--tri)"/>
    <rect x="38" y="40" width="14" height="19" fill="none" stroke="var(--maroon)" stroke-width="1.5"/>
    <line x1="41" y1="45" x2="49" y2="45" stroke="var(--maroon)" stroke-width="1.2"/>
    <line x1="41" y1="49" x2="47" y2="49" stroke="var(--maroon)" stroke-width="1.2"/>
    <circle cx="53" cy="58" r="5" fill="var(--tri)" stroke="var(--maroon)" stroke-width="1.5"/>
  </svg>
  <div class="offer-title">TAX AND REGULATORY</div>
  <p class="offer-text">Lorem Ipsum is simply dummy text of the printing and typesetting industry. Lorem Ipsum has been the industry's standard dummy text ever</p>
</div>

<section class="provide-band"></section>
<h2 class="section-title" style="top:625px">WHAT WE PROVIDE ?</h2>

<svg class="provide-card" style="left:85px;top:674px" width="262" height="151" viewBox="0 0 262 151">
  <defs><linearGradient id="gPhotoA" x1="0" y1="0" x2="1" y2="1"><stop offset="0" stop-color="#d0d0d0"/><stop offset="1" stop-color="#5e5e5e"/></linearGradient></defs>
  <polygon points="89,0 262,0 174,151" fill="url(#gPhotoA)" role="img" aria-label="Audience seated at a business conference, black and white"/>
  <polygon points="0,151 89,0 174,151" fill="var(--navy)" stroke="#fff" stroke-width="2"/>
  <g fill="#fff" font-family="Signika,sans-serif" font-size="14.5" font-weight="300" text-anchor="middle">
    <text x="85" y="103">CONSULTATIVE</text>
    <text x="85" y="120">SERVICES TO</text>
    <text x="85" y="137">BUSINESS C-SUITES</text>
  </g>
</svg>
<span class="plus">+</span>
<svg class="provide-card" style="left:354px;top:678px" width="264" height="150" viewBox="0 0 264 150">
  <defs><linearGradient id="gPhotoB" x1="0" y1="0" x2="1" y2="1"><stop offset="0" stop-color="#e0e0e0"/><stop offset="1" stop-color="#7a7a7a"/></linearGradient></defs>
  <polygon points="88,0 264,0 174,150" fill="url(#gPhotoB)" role="img" aria-label="Portrait of a smiling executive in a suit, black and white"/>
  <polygon points="0,150 88,0 174,150" fill="var(--maroon)" stroke="#fff" stroke-width="2"/>
  <g fill="#fff" font-family="Signika,sans-serif" font-size="14.5" font-weight="300" text-anchor="middle">
    <text x="88" y="100">PERSONAL</text>
    <text x="88" y="117">COACHING TO</text>
    <text x="88" y="134">EXECUTIVES.</text>
  </g>
</svg>
<p class="provide-text" style="left:85px;top:839px">Lorem Ipsum is simply dummy text of the printing and typesetting industry. Lorem Ipsum has been the industry's standard dummy text ever since the 1500s, when an unknown printer took a galley of type and scrambled</p>
<p class="provide-text" style="left:354px;top:839px">Lorem Ipsum is simply dummy text of the printing and typesetting industry. Lorem Ipsum has been the industry's standard dummy text ever since the 1500s, when an unknown printer took a galley of type and scrambled</p>

<section class="newsletter">
  <svg class="abs" style="left:102px;top:24px" width="17" height="13" viewBox="0 0 17 13"><rect x="1" y="1" width="15" height="11" fill="none" stroke="var(--maroon)" stroke-width="1.4"/><polyline points="1,1 8.5,7 16,1" fill="none" stroke="var(--maroon)" stroke-width="1.4"/></svg>
  <span class="nl-label">NEWSLETTER SIGN UP</span>
  <div class="nl-input">ENTER YOUR E-MAIL ADDRESS</div>
  <div class="nl-button">SUBSCRIBE NOW</div>
</section>

<footer>
  <div class="footer-rule" style="top:1003px"></div>
  <div class="footer-brand">
    <span class="brand-mark"></span>
    <span class="brand-name">BROOKVANE<br>COUNSEL PARTNERS</span>
  </div>

  <div class="footer-col" style="left:85px;width:67px">
    <div class="col-title">QUICK LINKS</div>
    <ul class="link-list"><li>Home</li><li>About Us</li><li>Services</li><li>Clients</li><li>Testimonials</li><li>Contact Us</li></ul>
  </div>
  <div class="footer-col" style="left:175px;width:123px">
    <div class="col-title">ABOUT US</div>
    <p class="col-text">Lorem Ipsum is simply dummy text of the printing and typesetting industry. Lorem Ipsum has been the industry's standard dummy text ever since the 1500s</p>
  </div>
  <div class="footer-col" style="left:313px;width:123px">
    <div class="col-title">NEWS</div>
    <div class="news-item"><div class="news-date">December 30th, 2015</div><p class="col-text">Lorem Ipsum is simply dummy text of the printing and typesetting industry.</p></div>
    <div class="news-item"><div class="news-date">December 30th, 2015</div><p class="col-text">Lorem Ipsum is simply dummy text of the printing and typesetting industry.</p></div>
  </div>
  <div class="footer-col" style="left:450px;width:125px">
    <div class="col-title">CONTACT US</div>
    <div class="contact-row"><svg width="8" height="8" viewBox="0 0 8 8"><polygon points="0,3 4,0 8,3" fill="var(--maroon)"/><rect x="1" y="3.5" width="1.2" height="3" fill="var(--maroon)"/><rect x="3.4" y="3.5" width="1.2" height="3" fill="var(--maroon)"/><rect x="5.8" y="3.5" width="1.2" height="3" fill="var(--maroon)"/><rect x="0" y="7" width="8" height="1" fill="var(--maroon)"/></svg><span>Brookvane Front Desk<br>Kelmarstraße 12<br>10115 Berlin | Germany</span></div>
    <div class="contact-row"><svg width="8" height="8" viewBox="0 0 8 8"><path d="M1,1 L3,1 L3.5,3 L2.5,3.8 Q3.5,5.5 4.5,5.5 L5.3,4.5 L7,5 L7,7 Q2,7.5 1,1Z" fill="var(--maroon)"/></svg><span>Telephone: +49 30 5550 1200</span></div>
    <div class="contact-row"><svg width="8" height="8" viewBox="0 0 8 8"><rect x="0.5" y="1.5" width="7" height="5" fill="none" stroke="var(--maroon)" stroke-width="1"/><polyline points="0.5,1.5 4,4.5 7.5,1.5" fill="none" stroke="var(--maroon)" stroke-width="1"/></svg><span>E-mail: hello@brookvane-mail.com</span></div>
  </div>

  <div class="footer-rule" style="top:1166px"></div>
  <span class="copyright">© 2015 Brookvane Counsel Partners | All Rights Reserved</span>
  <div class="social">Connect With Us <i></i><i></i><i></i><i></i><i></i></div>
</footer>

</body>
</html>
```